label redesign for skincare product

We would like a redesign of existing labels for a skincare product that we make (the existing labels are attached). This is a very natural product, but the existing labels are not right - one of the labels wraps around the jar, and one of the labels is placed on the bottom of the jar (copies of these attached). It needs softening and to be made less brutal looking. The label needs to communicate luxury quality product, that contains natural products, whilst maintaining a contemporary feel. The audience is male and female.

The product is called 'Dew Haven' and our company is called BR Naturals. We have a website at www.brnaturals-example.com where the existing product can be seen. It is NOT however necessary for the BR Naturals logo from the website to be used on the label - this is at the discretion of the designer.

The packaging will remain the same - this is a glass jar in extremely deep purple, almost black.

The colour of the product inside the jar is off white. The product contain mandarin and geranium essential oils so is floral and citrussy smelling.

Target Market(s)

Adults who like high quality natural skincare products, 30-65.

Industry/Entity Type

It Company

Font styles to use
Serif
Sans Serif

Colors

Designer to choose colors to be used in the design.

Requirements
Must have
• The long label must by 13mm high and 110 mm wide. The round label for the back of the jar must be 40mm diameter..

```html
<!DOCTYPE html>
<html lang="en">
<head>
<meta charset="utf-8">
<title>Dew Haven – Jar Labels</title>
<link rel="stylesheet" href="https://fonts.googleapis.com/css2?family=Marcellus&family=Source+Sans+3:wght@400;600;700&display=swap">
<style>
  :root {
    --plum: #4a1a6b;
    --plum-deep: #341f45;
    --peach: #fde0cc;
    --peach-light: #fff0e6;
    --orange: #f5a54a;
    --orange-soft: #f9c793;
    --white: #ffffff;
  }
  * { margin: 0; padding: 0; box-sizing: border-box; }
  html, body { width: 1200px; height: 900px; overflow: hidden; }
  body { font-family: "Source Sans 3", "Myriad Pro", sans-serif; color: var(--plum); }

  .canvas { position: relative; width: 1200px; height: 900px; background: var(--white); }
  .backdrop-band { position: absolute; left: 0; top: 594px; width: 1200px; height: 306px; background: var(--plum-deep); }

  /* Round back label */
  .round-label {
    position: absolute; left: 737px; top: 112px; width: 390px; height: 390px;
    border-radius: 50%; background: var(--peach);
    text-align: center; font-weight: 600; padding-top: 24px;
  }
  .round-label .product-name { font-size: 17px; font-weight: 700; line-height: 1.2; }
  .round-label .product-sub { font-size: 13px; margin-bottom: 10px; }
  .round-label .heading { font-size: 16px; font-weight: 700; line-height: 1.1; }
  .round-label .ingredients { font-size: 12.6px; line-height: 1.36; width: 350px; margin: 0 auto 10px; }
  .round-label .actives { font-size: 13px; line-height: 1.4; width: 300px; margin: 0 auto 8px; }
  .round-label .actives strong { font-size: 16px; font-weight: 700; }
  .round-label .note { font-size: 13px; margin-bottom: 12px; }
  .round-label .contact { font-size: 13px; line-height: 1.45; margin-bottom: 8px; }
  .round-label .volume { font-size: 15px; font-weight: 700; }

  /* Long wrap label */
  .wrap-label {
    position: absolute; left: 46px; top: 692px; width: 1108px; height: 112px;
    background: linear-gradient(90deg, var(--white) 0%, var(--white) 22%, var(--peach-light) 32%, var(--orange-soft) 44%, var(--orange) 49%, var(--orange-soft) 60%, var(--peach-light) 72%, var(--white) 82%);
    overflow: hidden;
  }
  .wrap-label .title-panel {
    position: absolute; left: 0; top: 0; width: 482px; height: 112px;
    background: linear-gradient(90deg, var(--white) 0%, var(--white) 40%, var(--peach-light) 75%, var(--orange-soft) 100%);
  }
  .wrap-label .stripe { position: absolute; left: 0; width: 482px; height: 3px;
    background: linear-gradient(90deg, var(--orange) 0%, var(--orange-soft) 50%, var(--orange) 100%); }
  .wrap-label .stripe.top-a { top: 13px; }
  .wrap-label .stripe.top-b { top: 22px; height: 2px; opacity: .6; }
  .wrap-label .stripe.bottom-a { top: 88px; height: 2px; opacity: .6; }
  .wrap-label .stripe.bottom-b { top: 96px; }
  .wrap-label .product-title {
    position: absolute; left: 46px; top: 26px;
    font-family: "Marcellus", "Optima", serif; font-size: 60px; line-height: 60px;
    color: var(--plum); letter-spacing: 1px; white-space: nowrap;
  }
  .wrap-label .copy {
    position: absolute; left: 491px; top: 11px; width: 442px;
    font-size: 10.6px; line-height: 15.6px; color: var(--plum);
  }
  .wrap-label .copy strong { font-weight: 700; }
</style>
</head>
<body>
<div class="canvas">
  <div class="backdrop-band"></div>

  <section class="round-label" aria-label="Back label">
    <p class="product-name">BR Naturals Dew Haven</p>
    <p class="product-sub">Moisturing salve for dry skin</p>
    <p class="heading">Ingredients:</p>
    <p class="ingredients">Helianthus Annuus (Sunflower) Oil, Prunus Dulcis (Sweet Almond) Oil, Cera Alba (beeswax), Vitis Vinifera (Grapeseed) Oil, Calendula Sylvestre (Calendula) Extract, Citrus Reticulata (Green Mandarin) Oil*, Pelargonium Graveolens Roseum (Geranium) Oil*, Benzyl Alcohol, Salicylic Acid, Glycerine, Sorbic Acid.</p>
    <p class="actives"><strong>Active ingredients:</strong> Cinnamal, Citronellol, Geraniol, Limonene, Linalool.</p>
    <p class="note">* Organic Ingredients</p>
    <p class="contact">support@brnaturals-example.com<br>www.brnaturals-example.com</p>
    <p class="volume">100MLe 3.2FL.OZ.</p>
  </section>

  <section class="wrap-label" aria-label="Wrap label">
    <div class="title-panel">
      <span class="stripe top-a"></span>
      <span class="stripe top-b"></span>
      <span class="stripe bottom-a"></span>
      <span class="stripe bottom-b"></span>
      <h1 class="product-title">DEW HAVEN</h1>
    </div>
    <p class="copy"><strong>BR Naturals Dew Haven with Calendula, Green Mandarin and Geranium.</strong><br>
      Moisturing salve for dry skin with naturally occuring active ingredients. Apply to dry skin that needs some love. Keep out of the reach of children. For external use only. Test on a small patch of skin before general application. Whilst unlikely, if you experience skin irritation stop using this product and consult a doctor. Store in a cool, dry place. No animal testing. BR Naturals, 14 Meadow Row, London E2 7QA. www.brnaturals-example.com</p>
  </section>
</div>
</body>
</html>
```